Simple psychologist website
Open brief, creative designs encouraged
Site map:
Home
our services
our psychologists
selective mutism
resources
contact

Current website:
http://mindsproutyouth.com.au/
Not in love with our logo, or colours etc - open brief
Happy for new font/style/logo for company name - if we choose a logo design from a designer who doesn't win the competition, we will award $50 for the logo and use it in the new website

Website made a few years ago for a sister company that we really like:
http://www.korrelpsychology.com.au/

Clean, credible and warm and friendly look & feel
stock photos OK, designer will be required to hand over any images used in the design as shown in the PSD

Target Market(s)

Adolescents with psychological issues and their families

Industry/Entity Type

Psychology

Number of Pages Required

2 page

Colors

Designer to choose colors to be used in the design.

Requirements
Must have
• One home page - simple with 2 or 3 small areas to tease and attract the user and one template page to suit all the other pages
• We like slides, we want to have 3 slides like korrelpsychology.com.au
• Three slide titles:
• 1. We specialise in many areas, find the right clinical psychologist for your family
• 2. Child Clinical Psychologists in Elmwood and Northgate
• 3. Resources
• Pages structurally similar to
• http://www.korrelpsychology.com.au/
• We like the 'featured' items, which in our case will have splash box titles (can be 3 or 4):
• 1. Selective Mutism
• 2. Is my child anxious?
• 3. Does my child have an eating disorder?
• 4. Parenting adolescents
• Does not need to be a copy of http://www.korrelpsychology.com.au/ and we are willing to accept outside-the-box thinking and design (we in fact encourage it)
• Owner of business wants to highlight Selective Mutism as they have specialists. Consider ways that may make this work.
• Design winner will be based on home page design but winning designer will be required to provide an additional but simpler 'standard' page template design based on the themes used in the winning design.

```html
<!DOCTYPE html>
<html lang="en">
<head>
<meta charset="utf-8">
<title>MindSprout – Child, Adolescent &amp; Family Psychology</title>
<link rel="stylesheet" href="https://fonts.googleapis.com/css2?family=Open+Sans:ital,wght@0,300;0,400;0,600;0,700;1,300;1,400&display=swap">
<style>
:root{
  --green:#8dc63f;
  --green-dark:#7ab32e;
  --ink:#222;
  --grey:#555;
  --white:#fff;
  --blue:#1a73e8;
  --nav-bg:rgba(40,40,40,.75);
}
*{box-sizing:border-box;margin:0;padding:0}
html,body{width:807px;height:1200px;overflow:hidden;background:var(--white);font-family:"Open Sans",Arial,sans-serif;color:var(--ink)}
.page{position:relative;width:807px;height:1200px}

.hero{position:absolute;left:0;top:0;width:807px;height:392px;overflow:hidden}
.hero-photo{position:absolute;inset:0;background:
  radial-gradient(circle at 62% 45%,rgba(230,80,110,.55),transparent 35%),
  radial-gradient(circle at 80% 30%,rgba(60,170,220,.45),transparent 30%),
  radial-gradient(circle at 70% 70%,rgba(240,190,40,.4),transparent 30%),
  linear-gradient(90deg,#cfcfcf 0%,#bdbdbd 35%,#e0e0e0 100%)}
.hero-shade{position:absolute;inset:0;background:rgba(30,30,40,.45)}
.nav{position:absolute;left:0;top:0;width:807px;height:38px;background:var(--nav-bg);display:flex;align-items:center}
.brand{position:absolute;left:158px;top:8px;color:var(--green);font-size:15px;font-weight:600;line-height:1}
.brand small{display:block;color:var(--white);font-size:4px;font-weight:600;margin-top:3px}
.nav-links{position:absolute;left:288px;top:14px;display:flex;gap:0;list-style:none;font-size:7.5px;color:var(--white)}
.nav-links li{margin-right:28px}
.nav-links li.active{color:var(--green)}
.hero-title{position:absolute;top:134px;width:100%;text-align:center;color:var(--green);font-size:21px;font-weight:700}
.hero-text{position:absolute;left:226px;top:172px;width:356px;text-align:center;color:var(--white);font-size:7px;line-height:9px}
.btn-outline{position:absolute;display:flex;align-items:center;justify-content:center;font-size:7px;text-transform:uppercase}
.hero .btn-outline{left:362px;top:238px;width:84px;height:25px;border:1px solid var(--white);color:var(--white)}
.dots{position:absolute;left:392px;top:361px;display:flex;gap:4px}
.dots span{width:5px;height:5px;border-radius:50%;background:var(--green)}
.dots span.on{background:transparent;border:1px solid var(--white);width:6px;height:6px;margin-top:-.5px}

.featured-head{position:absolute;top:416px;width:100%;text-align:center}
.featured-head::before,.featured-head::after{content:"";display:block;width:48px;height:2px;background:var(--green);margin:0 auto}
.featured-head h2{font-size:17px;font-weight:600;font-style:italic;margin:10px 0 12px}

.cards{position:absolute;top:482px;left:158px;display:flex;gap:13px}
.card{position:relative;width:155px;height:176px;overflow:hidden;color:var(--white)}
.card-photo{position:absolute;inset:0}
.card:nth-child(1) .card-photo{background:linear-gradient(135deg,#4a5f78,#2f4560)}
.card:nth-child(2) .card-photo{background:linear-gradient(135deg,#8a4a5a,#b23a3a 60%,#3a2a2a)}
.card:nth-child(3) .card-photo{background:linear-gradient(135deg,#6a7080,#4a5060)}
.card-shade{position:absolute;inset:0;background:rgba(20,30,50,.35)}
.card-frame{position:absolute;left:12px;top:13px;right:12px;bottom:13px;border:1.5px solid var(--white);text-align:center;padding:12px 8px 0}
.card h3{font-size:17px;font-weight:300;font-style:italic;line-height:20px}
.card p{font-size:6.8px;font-style:italic;line-height:9px;margin-top:8px}
.card .more{display:block;color:var(--green);font-size:7.5px;margin-top:4px}
.card:nth-child(3) .card-frame{padding-top:3px}

.more-post{left:362px;top:686px;width:84px;height:25px;border:1px solid var(--green);color:var(--green)}
.intro{position:absolute;left:158px;top:724px;width:492px;text-align:center;font-size:12.6px;font-weight:300;line-height:15.2px;color:var(--grey)}

.footer{position:absolute;left:0;top:872px;width:807px;height:278px;background:var(--green);color:var(--white)}
.footer h4{font-size:9.5px;font-weight:600;margin-bottom:8px}
.sitemap{position:absolute;left:158px;top:27px}
.sitemap ul{list-style:none;font-size:6px;line-height:13.5px}
.contact-form{position:absolute;left:240px;top:27px;width:268px}
.field{background:var(--white);height:20px;font-size:6px;color:#888;padding:7px 9px}
.row{display:flex;gap:3px;margin-bottom:4px}
.row .field{flex:1}
.field.wide{margin-bottom:4px}
.field.msg{height:77px}
.send{margin-top:3px;width:109px;height:25px;background:var(--blue);display:flex;align-items:center;justify-content:center;gap:10px;font-size:7px;font-weight:700;letter-spacing:1.5px}
.info{position:absolute;left:534px;top:30px;width:140px;font-size:6.5px;line-height:10px}
.info strong{display:block;font-weight:700;margin:6px 0 11px}
.info p{margin-bottom:8px}
.bottom-bar{position:absolute;left:0;top:1150px;width:807px;height:50px;display:flex;align-items:center;font-size:5px;letter-spacing:.6px;color:var(--grey);text-transform:uppercase}
.bottom-bar .copy{position:absolute;left:163px}
.bottom-bar .legal{position:absolute;left:558px;display:flex;gap:13px}
</style>
</head>
<body>
<div class="page">

  <header class="hero">
    <div class="hero-photo" role="img" aria-label="Illustration of a hand-drawn brain with colourful paint splashes"></div>
    <div class="hero-shade"></div>
    <nav class="nav">
      <div class="brand">MindSprout<small>Child, Adolescent &amp; Family Psychology</small></div>
      <ul class="nav-links">
        <li class="active">Home</li><li>Our Service</li><li>Our Psychologists</li><li>Selective Mutism</li><li>Resources</li><li>Contact</li>
      </ul>
    </nav>
    <h1 class="hero-title">RESOURCES</h1>
    <p class="hero-text">Lorem ipsum dolor sit amet, consectetur adipiscing elit. In interdum mollis consectetur. In hendrerit odio odio. Nullam malesuada vestibulum laoreet. Ut feugiat sed magna vel ultricies. Ut et suscipit quam. Etiam mollis neque in gravida efficitur. In placerat non massa non blandit. Morbi eu ligula efficitur, ornare libero nec, gravida diam. Maecenas feugiat dictum metus et blandit. Suspendisse quis lectus ac sapien mattis imperdiet. Aliquam risus libero, semper id purus ac, facilisis condimentum lacus. Aliquam varius est</p>
    <a class="btn-outline">Read more</a>
    <div class="dots"><span></span><span class="on"></span><span></span></div>
  </header>

  <div class="featured-head"><h2>Featured Post</h2></div>

  <section class="cards">
    <article class="card">
      <div class="card-photo" role="img" aria-label="Photo of a quiet young child"></div>
      <div class="card-shade"></div>
      <div class="card-frame">
        <h3>Selective<br>Mutism</h3>
        <p>Elena Varga, Clinical Psychologist at MindSprout Youth has many years of working with children with selective mutism. She is currently also ...</p>
        <span class="more">more</span>
      </div>
    </article>
    <article class="card">
      <div class="card-photo" role="img" aria-label="Photo of a worried child in a knitted hat"></div>
      <div class="card-shade"></div>
      <div class="card-frame">
        <h3>Is my child<br>anxious?</h3>
        <p>Understanding childhood anxiety Anxiety is a normal and sometimes helpful emotion in all children. Some children however, feel anxious more ...</p>
        <span class="more">more</span>
      </div>
    </article>
    <article class="card">
      <div class="card-photo" role="img" aria-label="Photo of a child at a table with a plate of food"></div>
      <div class="card-shade"></div>
      <div class="card-frame">
        <h3>Does my child<br>have an<br>eating disorder?</h3>
        <p>In summary, this article explains why eating disorders are dangerous and should be taken seriously. The main focus is on...</p>
        <span class="more">more</span>
      </div>
    </article>
  </section>

  <a class="btn-outline more-post">More post</a>

  <p class="intro">Everyone is susceptible to emotional issues at some stage in their life. It is harder than ever to stay content and degrees of anxiety and depression are inevitable.&nbsp; People have come to recognise the benefits of professional treatment for a better future. 1000’s of people have received help from us in the last 15 years. A change in your life can begin right now.&nbsp; We can help.</p>

  <footer class="footer">
    <div class="sitemap">
      <h4>Site Map</h4>
      <ul><li>Home</li><li>Our Services</li><li>Our Psychologists</li><li>Selective Mutism</li><li>Resources</li><li>Contact</li></ul>
    </div>
    <form class="contact-form">
      <h4>Contact Us at MindSprout</h4>
      <div class="row"><div class="field">Your Name</div><div class="field">Phone Number</div></div>
      <div class="field wide">Email Address</div>
      <div class="field msg">Message</div>
      <div class="send">SEND
        <svg width="18" height="10" viewBox="0 0 18 10" fill="none" stroke="#fff" stroke-width="1"><rect x="6" y="1" width="11" height="8"/><path d="M6 1l5.5 4.5L17 1M0 3h4M1 5h3M0 7h4"/></svg>
      </div>
    </form>
    <div class="info">
      <h4>Contact Information</h4>
      <svg width="8" height="11" viewBox="0 0 8 11"><path d="M4 0a4 4 0 0 1 4 4c0 3-4 7-4 7S0 7 0 4a4 4 0 0 1 4-4z" fill="#fff"/><circle cx="4" cy="4" r="1.5" fill="#8dc63f"/></svg>
      <strong>NORTHGATE</strong>
      <p>Suite 12, level 2<br>The Riverside Health Centre<br>48 Larkspur Road<br>Northgate NSW 2199</p>
      <strong>ELMWOOD</strong>
      <p>Suite 7C,<br>14-16 Fern Street<br>Elmwood NSW 2088</p>
      <svg width="10" height="10" viewBox="0 0 10 10" style="margin-top:8px"><path d="M2 1l2 2-1 1.5c.8 1.5 1.8 2.5 3 3L7.5 6l2 2-1.5 1.5C5 9 1 5 .5 2.5z" fill="#fff"/></svg>
      <p>Phone : 0400 555 218<br>Fax :&nbsp; (02) 5550 4417</p>
    </div>
  </footer>

  <div class="bottom-bar">
    <span class="copy">© Copyright 2017 MindSprout. All right reserved</span>
    <span class="legal"><span>Privacy Policy</span><span>Terms of Use</span></span>
  </div>

</div>
</body>
</html>
```